Real Estate - Large Sign Design

I am looking for a fresh new look for our leasing signs that will be showcase in front of commercial buildings available for lease. The sign dimension can be either 8'x4' or 4'x8'. They must exemplify our brand (see attachments) and be very visible by people driving by at high speeds.
They must include the following:
- Our logo (vector attached)
- Office Space Available
- 555-018-3274
- Nell Ruby
- Carl Ivey
- www.vantorile.com
Please let me know if you have any questions.
Target Market(s)
Drivers in high traffic areas, walking crowds
Industry/Entity Type
Real Estate
Requirements
Must have
- They must include the following:
- - Our logo (vector attached)
- - Office Space Available
- - 555-018-3274
- - Nell Ruby
- - Carl Ivey
- - www.vantorile.com
Should not have
- Should not be busy or hard to read.

```html
<!DOCTYPE html>
<html lang="en">
<head>
<meta charset="utf-8">
<title>Office Space Available – Leasing Sign</title>
<link rel="stylesheet" href="https://fonts.googleapis.com/css2?family=Oswald:wght@700&family=Open+Sans:wght@400;700;800&display=swap">
<style>
  :root {
    --brand-green: #00a651;
    --leaf-green: #2dbb6a;
    --lime: #c4d95a;
    --slate: #3a4658;
    --ink: #000000;
    --band-dark: #061c25;
    --paper: #ffffff;
    --canvas: #ececec;
  }
  html, body {
    margin: 0;
    width: 1200px;
    height: 1200px;
    overflow: hidden;
    background: var(--canvas);
  }
  .stage {
    position: relative;
    width: 1200px;
    height: 1200px;
  }
  .sign {
    position: absolute;
    left: 40px;
    top: 320px;
    width: 1360px;
    height: 680px;
    transform: scale(0.8235);
    transform-origin: 0 0;
    background: var(--paper);
    overflow: hidden;
    font-family: "Open Sans", sans-serif;
  }
  .sign-art {
    position: absolute;
    inset: 0;
  }
  .headline {
    position: absolute;
    left: 68px;
    top: 96px;
    margin: 0;
    font-family: "Oswald", sans-serif;
    font-weight: 700;
    font-size: 112px;
    line-height: 1.2;
    color: var(--brand-green);
    white-space: nowrap;
  }
  .phone {
    position: absolute;
    left: 195px;
    top: 258px;
    margin: 0;
    font-weight: 800;
    font-size: 150px;
    line-height: 1.2;
    letter-spacing: 2px;
    color: var(--ink);
    white-space: nowrap;
  }
  .agents {
    position: absolute;
    left: 0;
    width: 1320px;
    top: 410px;
    margin: 0;
    text-align: center;
    font-weight: 800;
    font-size: 80px;
    line-height: 1.2;
    color: var(--brand-green);
    white-space: nowrap;
  }
  .agents .divider { color: var(--ink); }
  .website {
    position: absolute;
    left: 0;
    width: 1360px;
    top: 556px;
    margin: 0;
    text-align: center;
    font-weight: 400;
    font-size: 92px;
    line-height: 1.2;
    letter-spacing: 0.2em;
    color: var(--paper);
    white-space: nowrap;
  }
  .company-name {
    position: absolute;
    right: 24px;
    top: 34px;
    margin: 0;
    text-align: center;
    font-weight: 400;
    font-size: 22px;
    line-height: 1.05;
    color: var(--paper);
  }
</style>
</head>
<body>
<main class="stage">
  <section class="sign" aria-label="Office space available leasing sign">
    <svg class="sign-art" viewBox="0 0 1360 680" aria-hidden="true">
      <defs>
        <linearGradient id="accent-top" x1="0" y1="0" x2="1" y2="0">
          <stop offset="0" stop-color="var(--lime)"/>
          <stop offset="0.55" stop-color="var(--leaf-green)"/>
          <stop offset="1" stop-color="var(--brand-green)"/>
        </linearGradient>
        <linearGradient id="accent-fade" x1="0" y1="0" x2="0" y2="1">
          <stop offset="0" stop-color="var(--brand-green)"/>
          <stop offset="0.35" stop-color="#3f9a6e"/>
          <stop offset="1" stop-color="var(--slate)"/>
        </linearGradient>
      </defs>
      <polygon class="accent-top" points="445,0 1360,0 1360,140 1205,115" fill="url(#accent-top)"/>
      <polygon class="accent-fade" points="1205,115 1360,140 1360,460" fill="url(#accent-fade)"/>
      <polygon class="accent-corner" points="1150,0 1360,0 1360,140 1205,115" fill="var(--brand-green)" opacity="0.85"/>
      <rect class="headline-rule" x="67" y="233" width="1153" height="6" fill="var(--brand-green)"/>
      <g class="phone-icon">
        <circle cx="122" cy="348" r="50" fill="none" stroke="var(--ink)" stroke-width="6"/>
        <path d="M103 318 q-10 8 -6 26 q8 30 34 42 q14 6 22 -4 l-14 -14 q-6 6 -12 2 q-14 -10 -18 -24 q-2 -7 5 -10 z"
              fill="var(--brand-green)"/>
      </g>
      <rect class="footer-rule" x="0" y="535" width="1360" height="7" fill="var(--brand-green)"/>
      <rect class="footer-band" x="0" y="542" width="1360" height="138" fill="var(--band-dark)"/>
    </svg>

    <p class="company-name">Vantorile<br>Property<br>Company</p>
    <h1 class="headline">OFFICE SPACE AVAILABLE</h1>
    <p class="phone">555-018-3274</p>
    <p class="agents">NELL RUBY <span class="divider">•</span> CARL IVEY</p>
    <p class="website">www.vantorile.com</p>
  </section>
</main>
</body>
</html>
```